Professional Learning Organization for Educators needs a Design Thinking Workshop Flyer

We need a flyer for a series of Introductory Design Thinking workshops we're delivering for education leaders.

We have generated our own version of the flyer with a word template, but want it to look even more professional and eye catching. It is attached.

We had an image that we thought might be good, but pulled it out so we don't bias designers' thinking.
Updates

Reason: We are a bit flexible on the deadline since this is a holiday week and people are traveling

Target Market(s)

Very busy education leaders whose curiosity needs to be stimulated enough to enroll in the course

Industry/Entity Type

Education

Font styles to use
Other font styles liked:
• Century Gothic or something closer to that

Requirements
Must have
• Some version of the text that is on the current flyer that I attached.
Nice to have
• I am very flexible and open right now on this design.

```html
<!DOCTYPE html>
<html lang="en">
<head>
<meta charset="utf-8">
<title>Design Thinking Workshops</title>
<link href="https://fonts.googleapis.com/css2?family=Jost:wght@300;400;500;600&display=swap" rel="stylesheet">
<style>
  :root {
    --teal: #4fb1a6;
    --teal-soft: #b9e2de;
    --ink: #1f2a2a;
    --text: #2d2d2d;
    --paper: #ffffff;
  }
  * { margin: 0; padding: 0; box-sizing: border-box; }
  html, body { width: 880px; height: 1200px; overflow: hidden; background: var(--paper); }
  body { font-family: "Jost", "Century Gothic", sans-serif; color: var(--text); }
  .flyer { position: relative; width: 880px; height: 1200px; background: var(--paper); }

  .edge { position: absolute; top: 0; height: 1200px; background: var(--teal); }
  .edge-left-wide { left: 0; width: 12px; }
  .edge-left-thin { left: 18px; width: 3px; }
  .edge-left-inner { left: 26px; width: 2px; }
  .edge-right-wide { right: 0; width: 12px; }
  .edge-right-thin { right: 16px; width: 3px; }
  .divider-a { left: 636px; width: 3px; }
  .divider-b { left: 645px; width: 2px; }

  .hero {
    position: absolute; left: 30px; top: 30px; width: 607px; height: 325px;
    background: linear-gradient(135deg, #3f6a64 0%, #2f524e 45%, #5e8a86 75%, #c9d4da 100%);
  }

  .band { position: absolute; left: 30px; width: 606px; background: var(--teal-soft); }

  .title-band { top: 382px; height: 46px; display: flex; align-items: center; justify-content: center; }
  .title { font-weight: 500; font-size: 28px; letter-spacing: 0.3px; color: var(--ink); }

  .intro { position: absolute; left: 59px; top: 456px; width: 560px; font-size: 17px; line-height: 27px; font-weight: 300; }
  .intro .tagline { font-weight: 500; margin-bottom: 13px; }
  .intro strong { font-weight: 600; }

  .benefits-band { top: 631px; height: 130px; }
  .benefits { list-style: none; position: absolute; left: 86px; top: 638px; width: 540px; font-size: 17px; line-height: 23px; font-weight: 300; }
  .benefits li { position: relative; padding-left: 28px; }
  .benefits svg { position: absolute; left: 0; top: 5px; }

  .schedule-note { position: absolute; left: 59px; top: 780px; width: 560px; font-size: 17px; line-height: 24px; font-weight: 300; }

  .dates-band { top: 897px; height: 114px; }
  .dates { list-style: none; position: absolute; left: 82px; top: 906px; font-size: 17px; line-height: 24px; font-weight: 500; }
  .dates li { position: relative; padding-left: 32px; }
  .dates svg { position: absolute; left: 0; top: 8px; }

  .details { position: absolute; left: 59px; top: 1044px; font-size: 17px; line-height: 24px; font-weight: 300; }

  .sidebar { position: absolute; left: 655px; top: 0; width: 211px; height: 1200px; background: var(--teal-soft); }
  .sidebar-gap { position: absolute; left: 655px; top: 900px; width: 211px; height: 110px; background: var(--paper); }
  .sidebar-head { position: absolute; left: 670px; top: 73px; width: 190px; text-align: center; font-size: 17px; line-height: 27px; font-weight: 500; color: var(--ink); }
  .quote { position: absolute; left: 669px; width: 190px; font-size: 17px; line-height: 27.3px; font-weight: 500; color: var(--ink); }
  .quote-1 { top: 182px; }
  .quote-2 { top: 427px; }
  .quote-3 { top: 646px; }
  .contact { position: absolute; left: 662px; top: 1042px; width: 200px; text-align: center; font-size: 16px; line-height: 27px; font-weight: 500; color: var(--ink); }
</style>
</head>
<body>
<main class="flyer">
  <div class="edge edge-left-wide"></div>
  <div class="edge edge-left-thin"></div>
  <div class="edge edge-left-inner"></div>
  <div class="edge edge-right-wide"></div>
  <div class="edge edge-right-thin"></div>
  <div class="edge divider-a"></div>
  <div class="edge divider-b"></div>

  <div class="hero" role="img" aria-label="Photo of hands writing numbers in chalk on a green chalkboard"></div>

  <div class="band title-band"><h1 class="title">DESIGN THINKING WORKSHOPS</h1></div>

  <section class="intro">
    <p class="tagline">Designing your way to better solutions.</p>
    <p>Ridgeline Public Schools and Summit Valley <strong>BOCES</strong> invite you to discover the power of Design Thinking. During our three session course, you will learn and practice mindsets and tools that help you continuously and creatively improve the experiences of the people you serve by:</p>
  </section>

  <div class="band benefits-band"></div>
  <ul class="benefits">
    <li><svg width="14" height="16" viewBox="0 0 14 16"><path d="M1 9 L5 14 L13 1" fill="none" stroke="#3fa89c" stroke-width="2.4" stroke-linecap="round" stroke-linejoin="round"/></svg>Understanding what your teachers, students and community truly need in their learning and work experiences.</li>
    <li><svg width="14" height="16" viewBox="0 0 14 16"><path d="M1 9 L5 14 L13 1" fill="none" stroke="#3fa89c" stroke-width="2.4" stroke-linecap="round" stroke-linejoin="round"/></svg>Designing solutions that better meet their needs.</li>
    <li><svg width="14" height="16" viewBox="0 0 14 16"><path d="M1 9 L5 14 L13 1" fill="none" stroke="#3fa89c" stroke-width="2.4" stroke-linecap="round" stroke-linejoin="round"/></svg>Seeking authentic feedback and reactions to these solutions prior to their implementation.</li>
  </ul>

  <p class="schedule-note">We are offering this three-session course at four different times in spring semester. Please choose the course that works best for your schedule.</p>

  <div class="band dates-band"></div>
  <ul class="dates">
    <li><svg width="24" height="10" viewBox="0 0 24 10"><path d="M0 5 H21 M16 1 L22 5 L16 9" fill="none" stroke="#3fa89c" stroke-width="1.8"/></svg>Monday mornings: 1/23, 1/30 and 2/6</li>
    <li><svg width="24" height="10" viewBox="0 0 24 10"><path d="M0 5 H21 M16 1 L22 5 L16 9" fill="none" stroke="#3fa89c" stroke-width="1.8"/></svg>Tuesday afternoons: 2/7, 2/14 and 2/21</li>
    <li><svg width="24" height="10" viewBox="0 0 24 10"><path d="M0 5 H21 M16 1 L22 5 L16 9" fill="none" stroke="#3fa89c" stroke-width="1.8"/></svg>Wednesday afternoons: 3/8, 3/15 and 3/22</li>
    <li><svg width="24" height="10" viewBox="0 0 24 10"><path d="M0 5 H21 M16 1 L22 5 L16 9" fill="none" stroke="#3fa89c" stroke-width="1.8"/></svg>Wednesday evenings: 2/8, 2/15 and 2/22</li>
  </ul>

  <section class="details">
    <p>Go to www.svboces.org to learn more.</p>
    <p>This course is held in Ridgeline Public Schools.</p>
    <p>No fee for RPS leaders.</p>
    <p>$150 fee for leaders outside of RPS.</p>
  </section>

  <aside>
    <div class="sidebar"></div>
    <div class="sidebar-gap"></div>
    <p class="sidebar-head">What our participants say…</p>
    <p class="quote quote-1">“This has been an empowering experience that allowed me to try out dramatic changes in my practice that I wouldn’t have imagined before.”</p>
    <p class="quote quote-2">“I never realized how often I’ve guessed and assumed what our teachers and students need – now I have a way to stop guessing!”</p>
    <p class="quote quote-3">“I finally have tools to generate truly creative ideas that people actually embrace… because they meet their needs”</p>
    <div class="contact">
      <p>SUMMIT VALLEY BOCES</p>
      <p>www.svboces.org</p>
      <p>Questions?</p>
      <p>j.morgan@svboces.org</p>
    </div>
  </aside>
</main>
</body>
</html>
```